Stationary and business cards for Meridale Wellness Clinic
Brightwater Meridale Wellness Clinic
Stationary and business cards for Meridale Wellness Clinic - Health
Creative Brief
Use same font as used in my logo
Use whatever fonts you feel works with the logo
Bright & Fun-filled
Dr. Marcus T. Falk
Chiropractic Physician
5182 Orvalle Park Rd. Ste. B Sarasota, FL 34871
wellpath7crew@mailnest.example
www.falkspinecare.example
when they go to the website, they need to click on other services in the top right of the page, and go to: functional endocrine, to read about what I do . I'm not sure how we can direct them to do that on a business card. Also, this is a separate business located within Falk Chiropractic Center,and has nothing to do with Chiropractic Care...... Use whatever fonts you feel works with the logo, or the same as the logo
Lack of energy, sleep problems, weight gain, and body pains are not normal processes of aging...You don't have to live with it! Call us today to reserve a seat at our next free seminar to learn how we can help you!

```html
<!DOCTYPE html>
<html lang="en">
<head>
<meta charset="utf-8">
<title>Business Card – Brightwater Meridale Wellness Clinic</title>
<link rel="stylesheet" href="https://fonts.googleapis.com/css2?family=Noto+Serif:wght@400;700&display=swap">
<style>
  :root {
    --backdrop: #4b4b4d;
    --card: #ffffff;
    --green: #3f9a12;
    --green-dark: #2c7a0b;
    --green-light: #6cc02b;
    --orange: #ef6f0f;
    --ink: #3c3c3c;
    --rule: #c9c9c9;
    --white: #ffffff;
  }
  * { margin: 0; padding: 0; box-sizing: border-box; }
  html, body {
    width: 1200px; height: 780px; overflow: hidden;
    background: var(--backdrop);
  }
  .canvas {
    position: relative; width: 1200px; height: 780px;
    display: flex; align-items: center; justify-content: center;
  }
  .card {
    position: relative; width: 1000px; height: 580px;
    background: var(--card); border-radius: 26px; overflow: hidden;
    font-family: "Noto Serif", Georgia, serif;
    box-shadow: 0 10px 30px rgba(0,0,0,.35);
  }
  .card-band { position: absolute; inset: 0; width: 1000px; height: 580px; }
  .doctor {
    position: absolute; top: 34px; right: 46px; text-align: right;
    color: var(--white); font-weight: 700;
  }
  .doctor-name { font-size: 31px; line-height: 1.2; }
  .doctor-title { font-size: 20px; line-height: 1.3; margin-top: 6px; }
  .divider {
    position: absolute; left: 468px; top: 270px; width: 2px; height: 230px;
    background: linear-gradient(var(--rule), #e9e9e9);
  }
  .brand {
    position: absolute; left: 60px; top: 356px; width: 380px;
  }
  .brand-name {
    color: var(--green); font-weight: 700;
    font-size: 25px; line-height: 1.3;
  }
  .contact {
    position: absolute; left: 492px; top: 270px;
    color: var(--ink); font-size: 18px; line-height: 1.45;
  }
  .address { margin-bottom: 26px; }
  .contact-list { list-style: none; }
  .contact-list li { display: flex; align-items: center; gap: 10px; height: 30px; }
  .contact-list svg { width: 20px; height: 20px; flex: none; }
</style>
</head>
<body>
<main class="canvas">
  <article class="card">
    <svg class="card-band" viewBox="0 0 1000 580" aria-hidden="true">
      <defs>
        <linearGradient id="bandGreen" x1="0" y1="0" x2="1" y2="1">
          <stop offset="0" stop-color="var(--green-light)"/>
          <stop offset="0.6" stop-color="var(--green)"/>
          <stop offset="1" stop-color="var(--green-dark)"/>
        </linearGradient>
      </defs>
      <path d="M0 0 H1000 V150 C820 185 620 110 420 128 C260 142 120 200 0 196 Z" fill="url(#bandGreen)"/>
      <path d="M0 196 C120 200 260 142 420 128 C620 110 820 185 1000 150 V170 C820 205 620 126 420 142 C260 156 120 214 0 212 Z" fill="var(--orange)"/>
    </svg>

    <header class="doctor">
      <p class="doctor-name">Dr. Marcus T. Falk</p>
      <p class="doctor-title">Chiropractic Physician</p>
    </header>

    <div class="brand">
      <p class="brand-name">Brightwater Meridale<br>Wellness Clinic</p>
    </div>

    <div class="divider"></div>

    <section class="contact">
      <p class="address">5182 Orvalle Park Rd. Ste. B<br>Sarasota, FL 34871</p>
      <ul class="contact-list">
        <li>
          <svg viewBox="0 0 20 20" aria-label="Phone"><path d="M5 2 L8 2 L9 6 L7 8 C8 10.5 9.5 12 12 13 L14 11 L18 12 L18 15 C18 17 16 18 14 17.5 C8 16 4 12 2.5 6 C2 4 3 2 5 2 Z" fill="var(--green)"/></svg>
          <span>941.555.0137</span>
        </li>
        <li>
          <svg viewBox="0 0 20 20" aria-label="Fax"><rect x="5" y="2" width="10" height="6" fill="none" stroke="var(--green)" stroke-width="2"/><rect x="2" y="8" width="16" height="7" rx="1.5" fill="var(--green)"/><rect x="5" y="13" width="10" height="5" fill="var(--green)" stroke="#fff" stroke-width="1"/></svg>
          <span>941.555.0148</span>
        </li>
        <li>
          <svg viewBox="0 0 20 20" aria-label="Email"><rect x="2" y="4" width="16" height="12" rx="1.5" fill="var(--green)"/><path d="M2.5 5 L10 11 L17.5 5" fill="none" stroke="#fff" stroke-width="1.5"/></svg>
          <span>wellpath7crew@mailnest.example</span>
        </li>
        <li>
          <svg viewBox="0 0 20 20" aria-label="Website"><circle cx="10" cy="10" r="8" fill="var(--green-light)"/><path d="M2 10 H18 M10 2 C6 6 6 14 10 18 M10 2 C14 6 14 14 10 18" fill="none" stroke="#fff" stroke-width="1"/></svg>
          <span>www.falkspinecare.example</span>
        </li>
      </ul>
    </section>
  </article>
</main>
</body>
</html>
```